Veltora Software Business Card Design

We are a new organization called Veltora. We are a software as a service provider. We deliver a project and program management solution via the internet, so everyone has the ability to work together and collaborate. Its an enterprise platform and we will focus on 50 plus employee company.

We have a website in place
www.veltora-demo.com

Use this as a start of producing the business card. The logo is there as well, but if you have a great and better solution...

Color scheme's could be inline with the website, but don't pin point on it. We can always change the website, logo, color scheme etc.

Target Market(s)

B2B, Projectmembers, projectmanagers, ICT, CTO, Marketing Managers

Industry/Entity Type

Software

Requirements
Must have
• Marten Kuyvelsma

Tel: +31 255 47 09 36
Mob: +31 6 927 15 062
marten@veltora-demo.com
Oostelingpad 84c
2184 KT Oosterwold

Www.veltora-demo.com
social media links

```html
<!DOCTYPE html>
<html lang="en">
<head>
<meta charset="utf-8">
<title>Veltora Business Card</title>
<link rel="stylesheet" href="https://fonts.googleapis.com/css2?family=Source+Sans+3:wght@300;400&display=swap">
<style>
  :root {
    --bg: #e6e6e6;
    --card-white: #ffffff;
    --lime: #b0f23c;
    --orange: #ff6a0a;
    --cyan: #00ffff;
    --ink: #111111;
    --paper-line: #ffffff;
  }
  * { margin: 0; padding: 0; box-sizing: border-box; }
  html, body {
    width: 1200px; height: 680px; overflow: hidden;
    background: var(--bg);
    font-family: "Source Sans 3", Arial, sans-serif;
    color: var(--ink);
  }
  .stage { position: relative; width: 1200px; height: 680px; }
  .card {
    position: absolute; top: 190px;
    width: 525px; height: 300px;
    overflow: hidden;
  }
  .card-front { left: 55px; background: var(--card-white); }
  .card-back { left: 620px; background: var(--cyan); }

  .bands { position: absolute; inset: 0; }

  .brand {
    position: absolute;
    display: flex; flex-direction: column; align-items: flex-end;
  }
  .front-brand { left: 88px; top: 96px; }
  .back-brand { left: 40px; top: 26px; }

  .brand-row { display: flex; align-items: center; gap: 14px; }
  .brand-mark { width: 22px; height: 22px; background: var(--cyan); }
  .back-brand .brand-mark { width: 18px; height: 18px; background: var(--paper-line); }
  .brand-name {
    font-weight: 300; font-size: 58px; line-height: 1;
    letter-spacing: 0.5px; color: var(--ink);
  }
  .back-brand .brand-name { font-size: 50px; }
  .tagline { font-weight: 400; font-size: 12.5px; margin-top: 4px; white-space: nowrap; }
  .back-brand .tagline { font-size: 10.5px; margin-top: 2px; }

  .holder {
    position: absolute; left: 42px; top: 118px;
    font-weight: 400; font-size: 17px;
  }
  .contact {
    position: absolute; left: 42px; top: 158px;
    list-style: none; font-weight: 400; font-size: 17px; line-height: 21px;
  }
  .website {
    position: absolute; right: 22px; bottom: 16px;
    font-weight: 400; font-size: 15px; color: var(--paper-line);
  }
</style>
</head>
<body>
<main class="stage">

  <section class="card card-front" aria-label="Card front">
    <svg class="bands" width="525" height="300" viewBox="0 0 525 300" aria-hidden="true">
      <rect x="0" y="22" width="525" height="26" fill="var(--lime)"/>
      <line x1="0" y1="16" x2="525" y2="48" stroke="var(--paper-line)" stroke-width="2"/>
      <rect x="0" y="248" width="525" height="24" fill="var(--orange)"/>
      <line x1="0" y1="246" x2="525" y2="258" stroke="var(--paper-line)" stroke-width="2"/>
    </svg>
    <div class="brand front-brand">
      <div class="brand-row">
        <span class="brand-mark"></span>
        <span class="brand-name">Veltora</span>
      </div>
      <p class="tagline">Simple, shared, visible and fully connected</p>
    </div>
  </section>

  <section class="card card-back" aria-label="Card back">
    <div class="brand back-brand">
      <div class="brand-row">
        <span class="brand-mark"></span>
        <span class="brand-name">Veltora</span>
      </div>
      <p class="tagline">Simple, shared, visible and fully connected</p>
    </div>
    <p class="holder">Marten Kuyvelsma</p>
    <ul class="contact">
      <li>Tel: +31 255 47 09 36</li>
      <li>Mob: +31 6 927 15 062</li>
      <li>marten@veltora-demo.com</li>
      <li>Oostelingpad 84c</li>
      <li>2184 KT Oosterwold</li>
    </ul>
    <p class="website">www.veltora-demo.com</p>
  </section>

</main>
</body>
</html>
```